Luxury Ayurvedic Hair Oil logo and package design

We need a logo and package design for our Ayurvedic and natural hair growth oil. Our company, Velmora, is the premier luxury Ayurvedic beauty brand, bringing ancient East-Indian natural and botanic health and beauty products to the US market. Our first major product - Velmora Hair Growth Oil - is a coconut oil based product that was developed by tribes in the Southern State of Kerala that includes ancient herbs like Gooseberry, Indigo, Indian Aloe, Balloon Vine and Brahmi.

The design should be catered to the high-end luxury market (minimal design, minimal text, fonts that invoke a sense of luxury). The primary colors should be deep blue for the packaging and gold for the characters (it's in the name - Velmora). We are looking to sell our products in Brenvale and Tolland Pryce and require packaging that is in line with products sold at these high-end retailers.

The final logo design and packaging should communicate luxury and the ancient wisdom of far-eastern traditions.

Target Market(s)

Velmora's main target is women who value fashionable/quality skincare, beauty, and fragrance products and are open to a medium to high price range. These women love uniqueness in brand and products that cannot be found elsewhere. They are looking for the next new "it" item that will take their haircare and beauty regiment to the next level.

Industry/Entity Type

Hair And Beauty

Font styles to use
Serif

Colors
2f73b3
ffc214

Requirements
Must have
• Must use deep blue (royal blue) background and gold text (to align with brand name). Must use luxurious fonts
Nice to have
• Flowers or other natural symbols, pictures that blend well with the product theme

```html
<!DOCTYPE html>
<html lang="en">
<head>
<meta charset="utf-8">
<title>Velmora Hair Growth Oil – Packaging</title>
<link href="https://fonts.googleapis.com/css2?family=Marcellus&family=Cabin+Condensed:wght@400;600&display=swap" rel="stylesheet">
<style>
  :root {
    --stage: #2b2c2e;
    --royal: #1f2a8f;
    --royal-deep: #18207a;
    --royal-light: #3e5bb8;
    --gold: #a98a2a;
    --gold-bright: #b8972f;
    --paper: #eef0f2;
    --paper-shade: #dfe2e6;
    --white: #ffffff;
  }
  * { box-sizing: border-box; margin: 0; padding: 0; }
  html, body { width: 1200px; height: 1104px; overflow: hidden; }
  body {
    background: var(--stage);
    position: relative;
    font-family: "Cabin Condensed", sans-serif;
  }
  .panel {
    position: absolute;
    background: linear-gradient(160deg, var(--paper) 0%, var(--paper-shade) 100%);
    overflow: hidden;
    text-align: center;
  }
  .panel svg.shape { position: absolute; left: 0; top: 0; }
  .panel .content { position: absolute; inset: 0; }

  /* Box side panel */
  .box-side { left: 150px; top: 120px; width: 180px; height: 860px; }
  /* Box front panel */
  .box-front { left: 330px; top: 120px; width: 300px; height: 860px; }
  /* Bottle label */
  .bottle-label { left: 720px; top: 360px; width: 320px; height: 480px; border-radius: 4px; }

  .brand-mark {
    display: block;
    border-radius: 50%;
    background: var(--white);
    margin: 0 auto;
  }
  .brand-name {
    font-family: "Marcellus", serif;
    color: var(--gold-bright);
    line-height: 1;
  }
  .brand-sub {
    font-family: "Marcellus", serif;
    color: var(--gold-bright);
    line-height: 1;
  }

  /* Front */
  .box-front .brand-mark { width: 62px; height: 62px; position: absolute; left: 119px; top: 44px; }
  .box-front .brand-name { position: absolute; left: 0; right: 0; top: 128px; font-size: 44px; }
  .box-front .brand-sub { position: absolute; left: 0; right: 0; top: 180px; font-size: 23px; }
  .title-hair {
    position: absolute; left: 0; right: 0; top: 330px;
    font-family: "Marcellus", serif; font-size: 104px; line-height: 1;
    color: var(--gold); letter-spacing: 1px;
  }
  .title-growth {
    position: absolute; left: 0; right: 0; top: 432px;
    font-family: "Marcellus", serif; font-size: 62px; line-height: 1;
    color: var(--royal);
  }
  .title-oil {
    position: absolute; left: 0; right: 0; top: 500px;
    font-family: "Marcellus", serif; font-size: 58px; line-height: 1;
    color: var(--gold);
  }
  .coconut-badge {
    position: absolute; left: 70px; top: 572px; width: 160px; height: 84px;
    background: var(--gold);
    border-radius: 4px 4px 80px 80px / 4px 4px 80px 80px;
    color: var(--white);
    font-family: "Marcellus", serif; font-size: 27px; line-height: 1.15;
    padding-top: 9px;
  }
  .herbs {
    position: absolute; left: 4px; right: 4px; top: 672px;
    font-family: "Cabin Condensed", sans-serif; font-weight: 600;
    font-size: 25px; line-height: 1.2; color: var(--royal);
    white-space: nowrap;
  }
  .volume {
    position: absolute; left: 60px; bottom: -100px; width: 180px; height: 180px;
    border-radius: 50%; background: var(--gold);
    color: var(--white); font-size: 28px; padding-top: 22px;
  }

  /* Side */
  .box-side .brand-mark { width: 44px; height: 44px; position: absolute; left: 68px; top: 60px; }
  .box-side .brand-name { position: absolute; left: 0; right: 0; top: 130px; font-size: 30px; }
  .box-side .brand-sub { position: absolute; left: 0; right: 0; top: 168px; font-size: 16px; }
  .side-copy { position: absolute; left: 18px; right: 18px; top: 318px; color: var(--royal-deep); }
  .side-heading {
    font-family: "Cabin Condensed", sans-serif; color: var(--gold);
    font-size: 19px; margin-bottom: 10px;
  }
  .side-text { font-size: 12.5px; line-height: 1.35; margin-bottom: 22px; }
  .side-notice {
    border: 1.5px solid var(--royal);
    padding: 10px 8px; font-size: 12.5px; line-height: 1.35;
  }

  /* Bottle label */
  .bottle-label .logo-row {
    position: absolute; left: 0; right: 0; top: 34px;
    display: flex; align-items: center; justify-content: center; gap: 12px;
  }
  .bottle-label .brand-mark { width: 52px; height: 52px; margin: 0; }
  .bottle-label .logo-text { text-align: left; }
  .bottle-label .brand-name { font-size: 32px; }
  .bottle-label .brand-sub { font-size: 15px; margin-top: 3px; }
  .label-hair {
    position: absolute; left: 0; right: 0; top: 166px;
    font-family: "Marcellus", serif; font-size: 96px; line-height: 1; color: var(--royal);
  }
  .label-growth {
    position: absolute; left: 0; right: 0; top: 258px;
    font-family: "Marcellus", serif; font-size: 40px; line-height: 1; color: var(--royal);
  }
  .label-band {
    position: absolute; left: 20px; right: 20px; top: 310px; height: 34px;
    background: var(--gold); border-radius: 4px 4px 20px 20px;
    color: var(--white); font-family: "Marcellus", serif; font-size: 22px;
    letter-spacing: 2px; line-height: 34px;
  }
  .label-herbs {
    position: absolute; left: 0; right: 0; top: 356px;
    font-weight: 600; font-size: 17px; line-height: 1.2; color: var(--royal);
  }
  .label-volume {
    position: absolute; left: 100px; bottom: -60px; width: 120px; height: 120px;
    border-radius: 50%; background: var(--gold);
    color: var(--white); font-size: 22px; padding-top: 20px;
  }
</style>
</head>
<body>

  <section class="panel box-side" aria-label="Box side panel">
    <svg class="shape" width="180" height="860" viewBox="0 0 180 860" aria-hidden="true">
      <defs>
        <linearGradient id="sideBlue" x1="0" y1="0" x2="1" y2="1">
          <stop offset="0" stop-color="var(--royal-deep)"/>
          <stop offset="1" stop-color="var(--royal)"/>
        </linearGradient>
      </defs>
      <path d="M0 0H180V290Q110 255 0 282Z" fill="url(#sideBlue)"/>
      <path d="M0 282Q110 255 180 290" fill="none" stroke="var(--gold)" stroke-width="4"/>
    </svg>
    <div class="content">
      <span class="brand-mark"></span>
      <p class="brand-name">Velmora</p>
      <p class="brand-sub">Hair Growth Oil</p>
      <div class="side-copy">
        <h3 class="side-heading">Ingredients:</h3>
        <p class="side-text">Virgin coconut oil, gooseberry, indigo, Indian aloe, balloon vine and brahmi, slow-infused in Kerala.</p>
        <h3 class="side-heading">How to use:</h3>
        <p class="side-text">Massage a few drops into the scalp. Leave overnight, then wash.</p>
        <p class="side-notice">For external use only. Store in a cool, dry place away from sunlight.</p>
      </div>
    </div>
  </section>

  <section class="panel box-front" aria-label="Box front panel">
    <svg class="shape" width="300" height="860" viewBox="0 0 300 860" aria-hidden="true">
      <defs>
        <linearGradient id="frontBlue" x1="1" y1="0" x2="0" y2="1">
          <stop offset="0" stop-color="var(--royal-deep)"/>
          <stop offset="0.55" stop-color="var(--royal-light)"/>
          <stop offset="1" stop-color="var(--royal)"/>
        </linearGradient>
      </defs>
      <path d="M0 0H300V290Q150 236 0 290Z" fill="url(#frontBlue)"/>
      <path d="M0 290Q150 236 300 290" fill="none" stroke="var(--gold)" stroke-width="4"/>
    </svg>
    <div class="content">
      <span class="brand-mark"></span>
      <p class="brand-name">Velmora</p>
      <p class="brand-sub">Hair Growth Oil</p>
      <h1 class="title-hair">HAIR</h1>
      <p class="title-growth">GROWTH</p>
      <p class="title-oil">OIL</p>
      <p class="coconut-badge">COCONUT<br>OIL</p>
      <p class="herbs">Gooseberry, Indigo,<br>Indian Aloe, Balloon<br>Vine and Brahmi</p>
      <p class="volume">50ml</p>
    </div>
  </section>

  <section class="panel bottle-label" aria-label="Bottle label">
    <svg class="shape" width="320" height="480" viewBox="0 0 320 480" aria-hidden="true">
      <path d="M0 0H320V150Q160 110 0 150Z" fill="var(--royal)"/>
      <path d="M0 150Q160 110 320 150" fill="none" stroke="var(--gold)" stroke-width="4"/>
    </svg>
    <div class="content">
      <div class="logo-row">
        <span class="brand-mark"></span>
        <div class="logo-text">
          <p class="brand-name">Velmora</p>
          <p class="brand-sub">Hair Growth Oil</p>
        </div>
      </div>
      <p class="label-hair">HAIR</p>
      <p class="label-growth">GROWTH OIL</p>
      <p class="label-band">COCONUT OIL</p>
      <p class="label-herbs">Gooseberry, Indigo, Indian Aloe,<br>Balloon Vine and Brahmi</p>
      <p class="label-volume">50ml</p>
    </div>
  </section>

</body>
</html>
```